Yard Sign Design for Roofing Contractor

We are looking for a new design for our yard signs used on all jobs we build. We are looking for a way to brand the company and are hoping that this contest can give us a "theme" we can incorporate into out other marketing items such as, vehicle graphics, apparel, etc... I have attached a copy of our logo to be used on the sign, it can be "shadowed" with a color to enhance the look and the sign, but please keep the basic logo design. Attached are some samples of construction colors the boss was thinking of along with a picture of our current yard sign to help give some direction and let you know what info is needed on the sign.The darker construction yellow may work better than the fluorescent yellow, but won't know without visual aid. We are not tied to any particular color as of now, so they do have freedom of design as long as keeping with the construction feel. (Just another thought, potentially a reflective construction tape look would be interesting so signs are visable at night)
Updates

Reason: Meeting with new web designers next week to discuss best option to incorporate into our website.Thank you for the submissions!

Target Market(s)

Want signs to stand out when driving by and visibility in neighborhood where sign is posted for potential referrals

Industry/Entity Type

Contractor

Colors
fbed22
fece3e
f37122

Requirements
Must have
• Information that is on our current signs, image attached. I uploaded a .pdf file showing some options that could work for adding "shading" to our logo if you choose to do so.
• Sign should measure 18" T, 24" W
Nice to have
• Interested is seeing designs using construction tape look, images attached

```html
<!DOCTYPE html>
<html lang="en">
<head>
<meta charset="utf-8">
<title>Stalwart Construction Yard Sign</title>
<link rel="stylesheet" href="https://fonts.googleapis.com/css2?family=Anton&family=Cinzel:wght@700;900&family=Nunito:wght@800&display=swap">
<style>
  :root {
    --backdrop: #e9e6e1;
    --hazard-yellow: #fbd52a;
    --hazard-black: #231f20;
    --panel-white: #ffffff;
    --panel-edge: #b9bcc0;
    --ink: #111111;
    --safety-orange: #f37122;
    --phone-white: #ffffff;
  }
  * { margin: 0; padding: 0; box-sizing: border-box; }
  html, body {
    width: 1200px;
    height: 750px;
    overflow: hidden;
    background: var(--backdrop);
  }
  .canvas {
    position: relative;
    width: 1200px;
    height: 750px;
    display: flex;
    align-items: center;
    justify-content: center;
  }
  .yard-sign {
    position: relative;
    width: 1000px;
    height: 750px;
    overflow: hidden;
    background: repeating-linear-gradient(
      -45deg,
      var(--hazard-black) 0 95px,
      var(--hazard-yellow) 95px 190px
    );
  }
  .brand-panel {
    position: absolute;
    left: 160px;
    top: 40px;
    width: 660px;
    height: 470px;
    background: var(--panel-white);
    border-radius: 26px;
    border: 10px solid var(--panel-edge);
    box-shadow: 0 8px 0 rgba(0,0,0,0.35);
    transform: rotate(3deg);
    display: flex;
    flex-direction: column;
    align-items: center;
    justify-content: center;
    text-align: center;
  }
  .brand-url {
    font-family: 'Nunito', sans-serif;
    font-weight: 800;
    font-size: 32px;
    color: var(--ink);
    margin-bottom: 18px;
  }
  .brand-name {
    font-family: 'Cinzel', serif;
    font-weight: 900;
    color: var(--ink);
    line-height: 1;
  }
  .brand-name .primary {
    display: block;
    font-size: 118px;
    letter-spacing: -2px;
  }
  .brand-name .secondary {
    display: block;
    font-size: 62px;
    margin-top: 6px;
  }
  .services {
    font-family: 'Cinzel', serif;
    font-weight: 700;
    font-size: 38px;
    color: var(--ink);
    margin-top: 34px;
    word-spacing: 10px;
  }
  .phone-row {
    position: absolute;
    left: 36px;
    top: 565px;
    display: flex;
    align-items: center;
    gap: 18px;
    transform: rotate(3deg);
  }
  .phone-icon {
    width: 120px;
    height: 120px;
    flex: none;
  }
  .phone-number {
    font-family: 'Anton', sans-serif;
    font-size: 142px;
    line-height: 1;
    color: var(--phone-white);
    -webkit-text-stroke: 6px var(--hazard-black);
    paint-order: stroke fill;
    letter-spacing: -1px;
  }
</style>
</head>
<body>
<main class="canvas">
  <section class="yard-sign" aria-label="Stalwart Construction yard sign">
    <div class="brand-panel">
      <p class="brand-url">www.stalwartroofing.com</p>
      <h1 class="brand-name">
        <span class="primary">STALWART</span>
        <span class="secondary">CONSTRUCTION</span>
      </h1>
      <p class="services">ROOF • SIDING • GUTTERS</p>
    </div>
    <div class="phone-row">
      <svg class="phone-icon" viewBox="0 0 120 120" aria-hidden="true">
        <circle cx="60" cy="60" r="56" fill="var(--safety-orange)" stroke="var(--phone-white)" stroke-width="6"/>
        <path d="M44 30 c4-3 8-2 10 2 l7 13 c2 4 1 7-2 9 l-5 3 c3 8 9 15 17 19 l3-5 c2-3 6-4 9-2 l13 7 c4 2 5 6 2 10 l-5 6 c-4 4-10 5-16 2 c-20-9-35-25-43-45 c-2-6-1-12 3-15 z" fill="var(--phone-white)"/>
      </svg>
      <p class="phone-number">405-555-0147</p>
    </div>
  </section>
</main>
</body>
</html>
```